New look while maintaining the Brand identification!

I want a new look for my business card. I want to keep the same colors and feel but change the look and layout a bit. The logo (KALMORETIX Physical therapy Reimagined and the lilypad) must remain the same and in that font.
We are a physical therapy clinic. So we have certification that we can write on the back or services we provide (which is what we currently have on the back of the card as well)

Contact information
2840 Cedar Hollow Rd., #22
Naples, FL 34276
P: (239) 555-0172
F: (239) 555-0198
E: kalmoretixcare@mailvexo.com
W: www.kalmoretixcare-example.com

Industry/Entity Type

Physical Therapy

Contact Information for Business Card

Our current cards have the business address and information on the back. But I am willing to have it be in the front.

Font styles to use
Sans Serif

Colors
abd036
fbf289
ec1f27

Requirements
Must have
• Has to be unique!
• Services we provide and/or techniques we do must fit on the card
Nice to have
• Would like to have the front and back somehow linked together. Such that if you set the front next to the back, there is a nice flow of design! Currently the back is white with writing on it.
Should not have
• I like the wave lines as compared to straight lines.

```html
<!DOCTYPE html>
<html lang="en">
<head>
<meta charset="utf-8">
<title>KALMORETIX Business Card</title>
<link href="https://fonts.googleapis.com/css2?family=Jost:wght@300;400;500;600&family=Tinos:ital@1&display=swap" rel="stylesheet">
<style>
  :root {
    --backdrop: #2a2a2a;
    --card-green: #98a63a;
    --name-olive: #6f7a2c;
    --card-white: #ffffff;
    --brand-gold: #cbab2b;
    --ink-gray: #4a4a4a;
    --icon-green: #8a9a32;
    --on-green: #f4f6e6;
  }
  * { margin: 0; padding: 0; box-sizing: border-box; }
  html, body {
    width: 1200px; height: 1200px; overflow: hidden;
    background: var(--backdrop);
  }
  .stage { position: relative; width: 1200px; height: 1200px; }
  .card {
    position: absolute;
    width: 720px; height: 411px;
    box-shadow: 0 10px 30px rgba(0,0,0,0.45);
  }
  /* Front card */
  .card-front {
    left: 400px; top: 130px;
    background: var(--card-green);
    font-family: "Jost", sans-serif;
  }
  .card-front .person {
    position: absolute; left: 40px; top: 150px;
  }
  .person-name {
    font-weight: 300; font-size: 56px; line-height: 1;
    color: var(--name-olive); letter-spacing: 1px;
  }
  .person-degrees {
    margin-top: 10px;
    font-weight: 400; font-size: 24px; color: var(--on-green);
    letter-spacing: 0.5px;
  }
  .person-certs {
    margin-top: 22px;
    font-family: "Tinos", serif; font-style: italic;
    font-size: 15px; line-height: 1.4; color: var(--on-green);
  }
  /* Back card */
  .card-back {
    left: 80px; top: 610px;
    background: var(--card-white);
    font-family: "Jost", sans-serif;
  }
  .brand-name {
    position: absolute; left: 40px; top: 60px;
    font-weight: 600; font-size: 42px; letter-spacing: 1px;
    color: var(--brand-gold);
  }
  .address {
    position: absolute; left: 40px; top: 180px;
    font-weight: 500; font-size: 20px; line-height: 1.35;
    letter-spacing: 2px; color: var(--ink-gray);
  }
  .contact-list {
    position: absolute; left: 40px; top: 262px;
    list-style: none;
  }
  .contact-item {
    display: flex; align-items: center; gap: 14px;
    font-weight: 500; font-size: 18px; line-height: 26px;
    color: var(--ink-gray); letter-spacing: 0.5px;
  }
  .contact-item svg { width: 16px; height: 16px; flex: none; }
</style>
</head>
<body>
<main class="stage">
  <section class="card card-front" aria-label="Business card front">
    <div class="person">
      <p class="person-name">Dana Corvell</p>
      <p class="person-degrees">PT, DPT, MSPT, MBA</p>
      <p class="person-certs">Certified Spinal Scoliosis Therapist.<br>Certified Equine Rehab Specialist. CAPP-OB</p>
    </div>
  </section>

  <section class="card card-back" aria-label="Business card back">
    <p class="brand-name">KALMORETIX</p>
    <p class="address">2840 Cedar Hollow Rd., #22<br>Naples, FL 34276</p>
    <ul class="contact-list">
      <li class="contact-item">
        <svg viewBox="0 0 16 16" fill="var(--icon-green)" aria-hidden="true"><path d="M2 5c0-2 2-3 6-3s6 1 6 3l-3 1-1-2H6L5 6 2 5zM4 8h8l2 6H2z"/></svg>
        (239) 555-0172
      </li>
      <li class="contact-item">
        <svg viewBox="0 0 16 16" fill="var(--icon-green)" aria-hidden="true"><rect x="4" y="1" width="8" height="14" rx="1.5"/><rect x="5.5" y="3" width="5" height="6" fill="#fff"/></svg>
        (239) 555-0198
      </li>
      <li class="contact-item">
        <svg viewBox="0 0 16 16" aria-hidden="true"><rect x="1" y="3" width="14" height="10" fill="var(--icon-green)"/><path d="M1 3l7 6 7-6" fill="none" stroke="#fff" stroke-width="1.3"/></svg>
        kalmoretixcare@mailvexo.com
      </li>
      <li class="contact-item">
        <svg viewBox="0 0 16 16" aria-hidden="true"><circle cx="9.5" cy="6.5" r="4.5" fill="none" stroke="var(--icon-green)" stroke-width="2"/><path d="M6.5 9.5L1.5 14.5" stroke="var(--icon-green)" stroke-width="2.4" stroke-linecap="round"/></svg>
        www.kalmoretixcare-example.com
      </li>
    </ul>
  </section>
</main>
</body>
</html>
```